IG ad to attract older men for better health #1

I want a bold headline Instagram Ad that coordinate with my website design with a racy sexy woman to attract men 45yrs old plus. See Two samples attached

Target Market(s)

Men 45 years old and older

Industry/Entity Type

Health And Wellness

Requirements
Must have
• eye catching appeal to men
Nice to have
• The copy to read
Blokes60up is the headline at the top of the page. Then the copy reads...
"I want to seduce you to better health with a little T&A. Remove the excuses, provide ridiculously simple tips and advice to get you started on a path of lasting heath." Want more?

```html
<!DOCTYPE html>
<html lang="en">
<head>
<meta charset="utf-8">
<title>Blokes60up – Instagram Ad</title>
<link rel="stylesheet" href="https://fonts.googleapis.com/css2?family=Bebas+Neue&family=Open+Sans:wght@700&display=swap">
<style>
  :root {
    --brand-red: #d71418;
    --brand-yellow: #f7c325;
    --text-white: #ffffff;
    --skin-light: #f3cfaa;
    --skin-mid: #e6b48a;
    --swim-yellow: #f5e020;
  }
  html, body {
    margin: 0;
    padding: 0;
    width: 1200px;
    height: 1200px;
    overflow: hidden;
    background: var(--brand-red);
  }
  .ad {
    position: relative;
    width: 1200px;
    height: 1200px;
    background: var(--brand-red);
    overflow: hidden;
    font-family: "Open Sans", Arial, sans-serif;
  }
  .ad__model {
    position: absolute;
    inset: 0;
    width: 1200px;
    height: 1200px;
  }
  .brand-name {
    position: absolute;
    left: 48px;
    top: 112px;
    margin: 0;
    font-family: "Open Sans", Arial, sans-serif;
    font-weight: 700;
    font-size: 64px;
    line-height: 1;
    color: var(--brand-yellow);
  }
  .brand-rule {
    position: absolute;
    left: 48px;
    top: 273px;
    width: 140px;
    height: 7px;
    background: var(--text-white);
  }
  .quote-mark {
    position: absolute;
    left: 40px;
    top: 318px;
    font-family: "Bebas Neue", "Oswald", sans-serif;
    font-size: 230px;
    line-height: 1;
    color: var(--brand-yellow);
  }
  .pull-quote {
    position: absolute;
    left: 48px;
    top: 440px;
    margin: 0;
    padding-left: 16px;
    border-left: 3px solid var(--text-white);
    font-family: "Bebas Neue", "Oswald", sans-serif;
    font-weight: 400;
    font-size: 80px;
    line-height: 76px;
    letter-spacing: -1.5px;
    color: var(--text-white);
  }
  .pull-quote p { margin: 0; }
  .supporting-copy {
    position: absolute;
    left: 66px;
    top: 741px;
    margin: 0;
    font-weight: 700;
    font-size: 31.5px;
    line-height: 42.5px;
    color: var(--text-white);
    text-transform: uppercase;
  }
  .cta {
    position: absolute;
    left: 46px;
    top: 1110px;
    width: 238px;
    height: 59px;
  }
  .cta svg {
    position: absolute;
    inset: 0;
  }
  .cta__label {
    position: absolute;
    left: 0;
    top: 0;
    width: 220px;
    height: 59px;
    display: flex;
    align-items: center;
    justify-content: center;
    font-weight: 700;
    font-size: 27px;
    color: var(--text-white);
    text-decoration: none;
  }
</style>
</head>
<body>
<main class="ad">
  <svg class="ad__model" viewBox="0 0 1200 1200" role="img" aria-label="Photo of a woman's torso in a yellow bikini, hand on hip">
    <defs>
      <linearGradient id="modelTone" x1="0" y1="0" x2="0" y2="1">
        <stop offset="0" stop-color="var(--skin-light)"/>
        <stop offset="0.25" stop-color="var(--swim-yellow)"/>
        <stop offset="0.4" stop-color="var(--skin-light)"/>
        <stop offset="0.8" stop-color="var(--skin-mid)"/>
        <stop offset="1" stop-color="var(--swim-yellow)"/>
      </linearGradient>
    </defs>
    <path d="M646 0 C560 200 500 380 512 489 C525 650 600 900 637 1200 L1200 1200 L1200 0 Z" fill="url(#modelTone)"/>
  </svg>

  <h1 class="brand-name">BLOKES60UP</h1>
  <div class="brand-rule"></div>

  <div class="quote-mark" aria-hidden="true">“</div>
  <blockquote class="pull-quote">
    <p>I want to</p>
    <p>seduce you to</p>
    <p>better health</p>
    <p>with a little T&amp;A.</p>
  </blockquote>

  <p class="supporting-copy">Remove the excuses,<br>provide ridiculously<br>simple tips and advice<br>to get you started on<br>a path of lasting health.</p>

  <div class="cta">
    <svg width="238" height="59" viewBox="0 0 238 59" aria-hidden="true">
      <path d="M2 2 H236 V36 L213 57 H2 Z" fill="none" stroke="var(--brand-yellow)" stroke-width="4"/>
    </svg>
    <span class="cta__label">WANT MORE?</span>
  </div>
</main>
</body>
</html>
```